Varga Lillas Physiotherapy Business Card Vienna

We need a business card design for a newly created Physiotherapy company based in Vienna Austria.
We seek a simple, modern, minimalist design without too much color variation. The font should look young/fresh, but definitely not childish or so. Since we are a starting Business, we currently haven't got a logo, if you feel like a logo would fit your design, feel free to use one, but it's not necessary.
Target Market(s)
Healthcare, young and elderly people with mobility issues
Industry/Entity Type
Health And Wellness
Contact Information for Business Card
Name: Lilla Varga
Title description: Physiotherapist
Phone num: +43 664 5290 4816
e-mail: lilla.praxis@brelomail.com
Colors
Designer to choose colors to be used in the design.
Requirements
Must have
- Final design language must be in German, basically, the Title Description needs to be "Physiotherapeutin" the other details remain as in the English Language.
Nice to have
- Simple, modern, minimalist design
Should not have
- too many colors, Obvious use of a skeleton, skull, spline

```html
<!DOCTYPE html>
<html lang="de">
<head>
<meta charset="utf-8">
<title>Lilla Varga – Visitenkarte</title>
<link rel="stylesheet" href="https://fonts.googleapis.com/css2?family=Open+Sans:wght@700&family=Kaushan+Script&display=swap">
<style>
  :root {
    --page-bg: #ffffff;
    --brand-blue: #00aeef;
    --band-blue: #3aa6df;
    --text-blue: #3a9fdb;
    --card-cream: #f6f3ec;
    --icon-green: #5e8e3e;
    --ornament-blue: #4aa8e0;
    --ornament-gold: #f0b73a;
    --white: #ffffff;
  }
  * { box-sizing: border-box; margin: 0; padding: 0; }
  html, body {
    width: 1200px; height: 1000px; overflow: hidden;
    background: var(--page-bg);
  }
  .canvas { position: relative; width: 1200px; height: 1000px; }
  .card {
    position: absolute; top: 136px; height: 720px;
    border-radius: 40px; overflow: hidden;
  }
  .card--front { left: 92px; width: 460px; background: var(--brand-blue); }
  .card--back { left: 632px; width: 458px; background: var(--card-cream); }

  .front-emblem {
    position: absolute; left: 264px; top: 331px; width: 116px; height: 116px;
    left: 172px; top: 195px;
    background: radial-gradient(circle, rgba(255,255,255,0.75) 0%, rgba(255,255,255,0.35) 70%, rgba(255,255,255,0) 100%);
    border-radius: 8px;
  }
  .front-title {
    position: absolute; left: 0; width: 100%; top: 339px;
    text-align: center; color: var(--white);
    font: 700 21px/1 "Open Sans", sans-serif;
  }

  .back-ornament {
    position: absolute; left: 23px; top: 32px; width: 123px; height: 124px;
    background: radial-gradient(circle, var(--ornament-gold) 0%, var(--ornament-blue) 60%, rgba(74,168,224,0) 72%);
    clip-path: polygon(50% 0, 100% 50%, 50% 100%, 0 50%);
  }
  .spine-band {
    position: absolute; left: 163px; width: 121px; background: var(--band-blue);
  }
  .spine-band--top { top: 0; height: 197px; }
  .spine-band--bottom { top: 547px; height: 173px; }

  .contact { position: absolute; left: 0; width: 100%; text-align: center; }
  .icon { position: absolute; left: 207px; }
  .icon--person { top: 215px; }
  .icon--phone { top: 368px; }
  .icon--mail { top: 456px; }
  .name, .role {
    position: absolute; left: 0; width: 100%; text-align: center;
    font: 400 38px/1 "Kaushan Script", cursive; color: var(--text-blue);
  }
  .name { top: 260px; }
  .role { top: 316px; }
  .phone, .email {
    position: absolute; left: 0; width: 100%; text-align: center;
    font-family: "Open Sans", sans-serif; font-weight: 700; color: var(--text-blue);
  }
  .phone { top: 410px; font-size: 30px; }
  .email { top: 503px; font-size: 23px; }
</style>
</head>
<body>
<main class="canvas">
  <section class="card card--front">
    <div class="front-emblem" role="img" aria-label="Weißes ornamentales Emblem"></div>
    <p class="front-title">Physiotherapeutin</p>
  </section>

  <section class="card card--back">
    <div class="back-ornament" role="img" aria-label="Blau-goldenes Mandala-Ornament"></div>
    <div class="spine-band spine-band--top" role="img" aria-label="Blaues Band mit stilisierter Wirbelsäule"></div>
    <div class="spine-band spine-band--bottom" role="img" aria-label="Blaues Band mit stilisierter Wirbelsäule"></div>

    <div class="contact">
      <svg class="icon icon--person" width="36" height="40" viewBox="0 0 36 40" aria-hidden="true">
        <circle cx="16" cy="11" r="9" fill="var(--icon-green)"/>
        <path d="M2 40 C2 26 30 26 30 40 Z" fill="var(--icon-green)"/>
        <circle cx="26" cy="31" r="7" fill="var(--icon-green)" stroke="var(--card-cream)" stroke-width="2"/>
        <path d="M26 27.5v7M22.5 31h7" stroke="var(--white)" stroke-width="2"/>
      </svg>
      <p class="name">Name: Lilla Varga</p>
      <p class="role">Physiotherapist</p>

      <svg class="icon icon--phone" width="38" height="34" viewBox="0 0 38 34" aria-hidden="true">
        <path d="M2 10 C2 2 36 2 36 10 L36 13 L28 13 L28 9 L10 9 L10 13 L2 13 Z" fill="var(--icon-green)"/>
        <path d="M8 14 L30 14 L35 32 L3 32 Z" fill="var(--icon-green)"/>
        <g fill="var(--card-cream)">
          <rect x="13" y="18" width="3" height="3"/><rect x="18" y="18" width="3" height="3"/><rect x="23" y="18" width="3" height="3"/>
          <rect x="12" y="23" width="3" height="3"/><rect x="18" y="23" width="3" height="3"/><rect x="24" y="23" width="3" height="3"/>
        </g>
      </svg>
      <p class="phone">+43 664 5290 4816</p>

      <svg class="icon icon--mail" width="38" height="32" viewBox="0 0 38 32" aria-hidden="true">
        <rect x="1" y="1" width="36" height="30" rx="3" fill="var(--icon-green)"/>
        <rect x="5" y="5" width="28" height="22" fill="var(--white)"/>
        <path d="M5 5 L19 19 L33 5" fill="none" stroke="var(--icon-green)" stroke-width="4"/>
      </svg>
      <p class="email">lilla.praxis@brelomail.com</p>
    </div>
  </section>
</main>
</body>
</html>
```